business card and stationary
Byte Haven Works
Modern
Martin Okonedo
Owner
2738 Larkin Avenue
Green Cove Springs FL 32043
bytehavenworks@mailnest.example
www.bytehavenworks.example
I don't want the address on the business card.
logo .ai file

```html
<!DOCTYPE html>
<html lang="en">
<head>
<meta charset="utf-8">
<title>Byte Haven Works — Stationery Set</title>
<link rel="stylesheet" href="https://fonts.googleapis.com/css2?family=Orbitron:wght@700&family=Open+Sans:wght@400;600&display=swap">
<style>
  :root{
    --canvas:#efe6d8;
    --paper:#ffffff;
    --navy:#1b2433;
    --blue:#2b6fd6;
    --blue-light:#5aa0f0;
    --ink:#2a2f38;
    --muted:#8a8f98;
    --faint:#e3e6ea;
    --label:#6b5a44;
  }
  *{box-sizing:border-box;margin:0;padding:0}
  html,body{width:1200px;height:446px;overflow:hidden}
  body{background:var(--canvas);font-family:"Open Sans",Arial,sans-serif;position:relative;color:var(--ink)}
  .sheet{position:absolute;background:var(--paper);box-shadow:0 2px 6px rgba(0,0,0,.25);overflow:hidden}
  .label{position:absolute;font-size:6px;letter-spacing:.5px;text-transform:uppercase;color:var(--label);text-align:center}
  .brand{display:flex;align-items:center;gap:4px;font-family:"Orbitron",sans-serif;font-weight:700;color:var(--navy);white-space:nowrap}
  .brand .mark{background:var(--navy)}
  .brand-faint{position:absolute;left:0;right:0;text-align:center;font-family:"Orbitron",sans-serif;font-weight:700;color:var(--faint);white-space:nowrap}
  .swoosh{position:absolute;left:0;bottom:0;width:100%}
  .contact{position:absolute;font-size:4px;line-height:6px;color:var(--muted)}

  .card{left:19px;width:125px;height:38px}
  .card-front{top:206px}
  .card-back{top:268px}
  .card .brand{position:absolute;left:0;right:0;top:8px;justify-content:center;font-size:8px}
  .card .brand .mark{width:6px;height:6px}
  .card .contact{top:19px;left:0;right:0;text-align:center}

  .letterhead{top:19px;width:228px;height:404px}
  .letterhead-1{left:163px}
  .letterhead-2{left:413px}
  .letterhead .brand{position:absolute;left:18px;top:18px;font-size:11px}
  .letterhead .brand .mark{width:8px;height:8px}
  .letterhead .brand-faint{top:190px;font-size:16px}
  .letterhead-1 .contact{right:16px;top:18px;text-align:right}
  .letterhead-2 .contact{left:0;right:0;bottom:22px;text-align:center}

  .envelope{left:679px;width:502px}
  .env-black{top:19px;height:72px;background:var(--navy)}
  .env-blue{top:96px;height:96px;background:linear-gradient(180deg,#1d55c0,#6fb0f5 45%,#1d55c0)}
  .env-white{top:197px;height:92px}
  .env-front{top:300px;height:120px}
  .flap{position:absolute;inset:0;width:100%;height:100%}
  .env-front .brand{position:absolute;left:18px;top:14px;font-size:11px}
  .env-front .brand .mark{width:8px;height:8px}
  .env-front .contact{left:18px;top:30px}
</style>
</head>
<body>

<p class="label" style="left:19px;top:190px;width:125px">Background Samples</p>

<section class="sheet card card-front">
  <div class="brand"><span class="mark"></span>Byte Haven Works</div>
  <p class="contact">Martin Okonedo · Owner</p>
  <svg class="swoosh" viewBox="0 0 125 12" preserveAspectRatio="none" height="12">
    <path d="M0 6 Q62 -2 125 6 L125 12 L0 12Z" fill="var(--blue)"/>
    <path d="M0 9 Q62 2 125 9 L125 12 L0 12Z" fill="var(--navy)"/>
  </svg>
</section>
<p class="label" style="left:19px;top:250px;width:125px">Business Card Front</p>

<section class="sheet card card-back">
  <div class="brand"><span class="mark"></span>Byte Haven Works</div>
  <p class="contact">bytehavenworks@mailnest.example<br>www.bytehavenworks.example</p>
  <svg class="swoosh" viewBox="0 0 125 12" preserveAspectRatio="none" height="12">
    <path d="M0 6 Q62 -2 125 6 L125 12 L0 12Z" fill="var(--blue)"/>
    <path d="M0 9 Q62 2 125 9 L125 12 L0 12Z" fill="var(--navy)"/>
  </svg>
</section>
<p class="label" style="left:19px;top:312px;width:125px">Business Card Back</p>

<section class="sheet letterhead letterhead-1">
  <div class="brand"><span class="mark"></span>Byte Haven Works</div>
  <p class="contact">2738 Larkin Avenue<br>Green Cove Springs FL 32043<br>www.bytehavenworks.example</p>
  <div class="brand-faint">Byte Haven Works</div>
  <svg class="swoosh" viewBox="0 0 228 28" preserveAspectRatio="none" height="28">
    <path d="M0 14 Q114 -4 228 14 L228 28 L0 28Z" fill="var(--blue)"/>
    <path d="M0 20 Q114 6 228 20 L228 28 L0 28Z" fill="var(--navy)"/>
  </svg>
</section>
<p class="label" style="left:163px;top:430px;width:228px">Letterhead Option 1</p>

<section class="sheet letterhead letterhead-2">
  <div class="brand"><span class="mark"></span>Byte Haven Works</div>
  <div class="brand-faint">Byte Haven Works</div>
  <p class="contact">2738 Larkin Avenue, Green Cove Springs FL 32043 · bytehavenworks@mailnest.example · www.bytehavenworks.example</p>
  <svg class="swoosh" viewBox="0 0 228 18" preserveAspectRatio="none" height="18">
    <path d="M0 8 Q114 -3 228 8 L228 18 L0 18Z" fill="var(--blue)"/>
    <path d="M0 12 Q114 3 228 12 L228 18 L0 18Z" fill="var(--navy)"/>
  </svg>
</section>
<p class="label" style="left:413px;top:430px;width:228px">Letterhead Option 2</p>

<section class="sheet envelope env-black">
  <svg class="flap" viewBox="0 0 502 72" preserveAspectRatio="none"><path d="M0 0 L251 60 L502 0" fill="none" stroke="#2c3850" stroke-width="2"/></svg>
</section>
<section class="sheet envelope env-blue">
  <svg class="flap" viewBox="0 0 502 96" preserveAspectRatio="none"><path d="M0 0 L251 70 L502 0" fill="none" stroke="#ffffff" stroke-opacity=".5" stroke-width="2"/></svg>
</section>
<section class="sheet envelope env-white">
  <svg class="flap" viewBox="0 0 502 92" preserveAspectRatio="none"><path d="M0 0 L251 66 L502 0" fill="none" stroke="#d5d8dc" stroke-width="1.5"/></svg>
</section>
<section class="sheet envelope env-front">
  <div class="brand"><span class="mark"></span>Byte Haven Works</div>
  <p class="contact">2738 Larkin Avenue<br>Green Cove Springs FL 32043</p>
  <svg class="swoosh" viewBox="0 0 502 22" preserveAspectRatio="none" height="22">
    <path d="M0 10 Q251 -4 502 10 L502 22 L0 22Z" fill="var(--blue)"/>
    <path d="M0 15 Q251 4 502 15 L502 22 L0 22Z" fill="var(--navy)"/>
  </svg>
</section>
<p class="label" style="left:679px;top:430px;width:502px">Envelope Option 1</p>

</body>
</html>
```